Wordpress Design - Accounting Practice Startup

We are a relatively new Accounting Firm in Sydney with a primary focus on the Not-For-Profit sector. We need a complete re-design of our wordpress based website: www.tallowmereledger.com.au
We already have a logo design which we would like to keep using. See uploaded files.
We have a simple menu stucture:
- Home
- About Us
- Our Services
- Contact Us
(Suggestions welcome!)
Happy for it to be a single page scrolling website linked via the menu. We would like the "Our Services" page/section to have icons for the following:
- Bookkeeping
- Payroll
- Accounting
- Training
- Consulting
- Projects
We'd like a banner at the top of the page below the menu, and a place for testimonials, possibly integrated into the body or to the side. Images and icons to be included would be great.
Our main aim is to have an elegant and modern website that works well on all devices.
Updates
Industry/Entity Type
Accounting
Colors
Designer to choose colors to be used in the design.
Look and feel
Each slider illustrates characteristics of the customer's brand and the style your logo design should communicate.

```html
<!DOCTYPE html>
<html lang="en">
<head>
<meta charset="utf-8">
<title>Tallowmere Ledger</title>
<link href="https://fonts.googleapis.com/css2?family=Roboto:wght@400;500&family=Roboto+Condensed:wght@400;700&family=Open+Sans:wght@400;600&display=swap" rel="stylesheet">
<style>
:root{
  --green:#43a03f;
  --ink:#1e1e1e;
  --text:#444;
  --muted:#666;
  --white:#fff;
  --footer:#1d1d1d;
  --footer-line:#3a3a3a;
  --navy:#2b5d84;
}
*{box-sizing:border-box;margin:0;padding:0}
html,body{width:1200px;height:2510px;overflow:hidden}
body{position:relative;background:var(--white);font-family:"Open Sans",sans-serif;color:var(--text)}
.abs{position:absolute}
h1,h2,h3{font-weight:400}

/* brand */
.brand{display:flex;align-items:center;gap:12px;font-family:"Roboto",sans-serif;font-weight:400;font-size:26px;line-height:27px;letter-spacing:1px;color:var(--ink)}
.brand-mark{flex:none;width:22px;height:22px;background:var(--green)}
.brand-name{display:block}

/* header */
.site-header{left:0;top:0;width:1200px;height:131px;background:var(--white)}
.header-brand{left:85px;top:40px}
.nav-link{top:54px;font-family:"Roboto",sans-serif;font-size:17px;line-height:20px;color:var(--ink);text-decoration:none}
.nav-link.active{color:var(--green)}
.search-icon{left:1090px;top:55px}

/* hero */
.hero{left:0;top:131px;width:1200px;height:527px;background:linear-gradient(135deg,#b9c0c8 0%,#8b939c 45%,#d3d7db 100%)}
.hero-title{left:0;top:335px;width:1200px;text-align:center;font-family:"Roboto Condensed",sans-serif;font-weight:700;font-size:53px;line-height:60px;color:var(--white);letter-spacing:.5px}
.hero-sub{left:0;top:405px;width:1200px;text-align:center;font-family:"Roboto Condensed",sans-serif;font-size:31px;line-height:36px;color:var(--white)}

/* about */
.about-frame{left:117px;top:785px;width:315px;height:325px;background:var(--green)}
.about-photo{left:140px;top:808px;width:309px;height:329px;background:linear-gradient(160deg,#e9e4dc,#c7b69a 55%,#8d9aa5);box-shadow:0 8px 20px rgba(0,0,0,.3)}
.about-title{left:492px;top:812px;font-family:"Roboto Condensed",sans-serif;font-size:36px;line-height:42px;color:var(--ink)}
.about-sub{left:492px;top:860px;font-family:"Roboto Condensed",sans-serif;font-size:22px;line-height:26px;color:var(--ink)}
.about-text{left:491px;top:897px;width:576px;font-size:14.4px;line-height:25.6px;text-align:justify;color:var(--text)}
.btn-more{left:490px;top:1087px;width:115px;height:34px;border-radius:17px;background:var(--green);color:var(--white);font-size:14px;display:flex;align-items:center;justify-content:center}

/* services */
.services{left:0;top:1233px;width:1200px;height:499px;background:linear-gradient(120deg,#3e9a3a 0%,#55ab50 55%,#86c681 100%)}
.services-title{left:0;top:1311px;width:1200px;text-align:center;font-family:"Roboto Condensed",sans-serif;font-size:34px;line-height:40px;color:var(--white)}
.service{display:flex;align-items:flex-start;gap:18px;color:var(--white)}
.service-icon{flex:none;width:84px;height:84px;border-radius:50%;background:var(--white);box-shadow:0 0 0 3px var(--green),0 0 0 5px rgba(255,255,255,.8);display:flex;align-items:center;justify-content:center}
.service-name{font-family:"Roboto Condensed",sans-serif;font-size:21px;line-height:24px;margin-top:4px}
.service-desc{font-size:12.5px;line-height:18px;margin-top:4px;white-space:nowrap}

/* testimonials */
.testi-title{left:0;top:1832px;width:1200px;text-align:center;font-family:"Roboto Condensed",sans-serif;font-size:30px;line-height:36px;color:var(--ink)}
.testimonial{display:flex;gap:18px}
.avatar{flex:none;width:92px;height:92px;border-radius:50%;background:linear-gradient(160deg,#b8c2cc,#6d7a86)}
.testi-body{width:352px}
.quote{position:relative;padding-left:22px;font-size:13.2px;line-height:22px;color:var(--muted);text-align:justify}
.quote-mark{color:var(--green);font-size:20px;font-family:"Roboto",sans-serif;line-height:0}
.quote-open{position:absolute;left:0;top:10px}
.person{margin-top:8px;padding-left:22px;font-size:11.5px;line-height:14px;color:var(--ink);text-transform:uppercase}
.role{padding-left:22px;font-size:13px;line-height:16px;color:var(--ink);margin-top:5px}

/* footer */
.site-footer{left:0;top:2193px;width:1200px;height:317px;background:linear-gradient(180deg,#262626,var(--footer))}
.footer-brand{left:87px;top:2293px;color:var(--white)}
.footer-brand .brand-mark{background:var(--white)}
.f-head{font-size:13.5px;line-height:16px;color:var(--white);text-transform:uppercase}
.f-list{font-size:12px;line-height:22px;color:var(--white);list-style:none;margin-top:18px}
.f-list li{display:flex;gap:14px}
.f-list svg{flex:none;margin-top:6px}
.f-note{font-size:12px;line-height:18px;color:var(--white);margin-top:16px;width:200px}
.signup{display:flex;margin-top:12px}
.signup .field{width:142px;height:30px;background:var(--white);font-size:11.5px;color:#888;padding:8px}
.signup .submit{width:62px;height:30px;background:var(--navy);color:var(--white);font-size:12px;display:flex;align-items:center;justify-content:center}
.socials{display:flex;gap:14px;margin-top:20px}
.socials span{width:24px;height:24px;border-radius:4px;background:var(--white)}
.f-rule{left:77px;top:2424px;width:1024px;height:1px;background:var(--footer-line)}
.copyright{left:0;top:2452px;width:1200px;text-align:center;font-size:12px;color:var(--white)}
</style>
</head>
<body>

<header class="abs site-header">
  <div class="abs brand header-brand"><span class="brand-mark"></span><span><span class="brand-name">TALLOWMERE</span><span class="brand-name">LEDGER</span></span></div>
  <a class="abs nav-link active" href="#home" style="left:611px">Home</a>
  <a class="abs nav-link" href="#about" style="left:701px">About us</a>
  <a class="abs nav-link" href="#services" style="left:815px">Our Services</a>
  <a class="abs nav-link" href="#contact" style="left:959px">Contact us</a>
  <svg class="abs search-icon" width="20" height="20" viewBox="0 0 20 20"><circle cx="8" cy="8" r="6" fill="none" stroke="#1e1e1e" stroke-width="2.6"/><line x1="12.5" y1="12.5" x2="18" y2="18" stroke="#1e1e1e" stroke-width="3" stroke-linecap="round"/></svg>
</header>

<section class="abs hero" id="home" role="img" aria-label="Photo of an accountant working at a desk with a laptop, calculator and financial charts"></section>
<h1 class="abs hero-title">TALLOWMERE LEDGER</h1>
<p class="abs hero-sub">Neque porro quisquam dolorem</p>

<section id="about">
  <div class="abs about-frame"></div>
  <div class="abs about-photo" role="img" aria-label="Top view of a desk with a laptop, phone and printed reports"></div>
  <h2 class="abs about-title">About</h2>
  <h3 class="abs about-sub">Tallowmere ledger</h3>
  <p class="abs about-text">At Tallowmere Ledger, we believe that every number counts. We strive to deliver a premium service at a reasonable cost. Our focus is to ensure your financial needs are met with the quality, integrity, diligence and timeliness that you would expect. Tallowmere Ledger originated with the idea of providing accounting services that would make clients feel safe and find refuge, feel confident that they could trust the numbers in their financial reports. The founders of Tallowmere Ledger migrated to Australia as refugees and the name of the business alludes to these origins.</p>
  <div class="abs btn-more">Read More &raquo;</div>
</section>

<section class="abs services" id="services" role="img" aria-label="Green-tinted background photo of a desk with paperwork"></section>
<h2 class="abs services-title">Our Services</h2>

<div class="abs service" style="left:92px;top:1414px">
  <div class="service-icon"><svg width="34" height="26" viewBox="0 0 34 26"><rect x="5" y="2" width="24" height="16" rx="1" fill="none" stroke="#43a03f" stroke-width="2.5"/><rect x="1" y="20" width="32" height="3" fill="#43a03f"/></svg></div>
  <div><div class="service-name">Bookkeeping</div><div class="service-desc">It has survived not only five centu-<br>ries,but also the leap into elec-</div></div>
</div>
<div class="abs service" style="left:442px;top:1414px">
  <div class="service-icon"><svg width="28" height="30" viewBox="0 0 28 30"><rect x="3" y="2" width="15" height="20" fill="#43a03f"/><rect x="10" y="9" width="15" height="19" fill="#fff" stroke="#43a03f" stroke-width="2.5"/></svg></div>
  <div><div class="service-name">Payroll</div><div class="service-desc">It has survived not only five centu-<br>ries,but also the leap into elec-</div></div>
</div>
<div class="abs service" style="left:802px;top:1414px">
  <div class="service-icon"><svg width="24" height="30" viewBox="0 0 24 30"><path d="M2 2h13l7 7v19H2z" fill="#43a03f"/><path d="M6 14h12M6 19h12M6 24h12" stroke="#fff" stroke-width="2"/></svg></div>
  <div><div class="service-name">Accounting</div><div class="service-desc">It has survived not only five centu-<br>ries,but also the leap into elec-</div></div>
</div>
<div class="abs service" style="left:92px;top:1545px">
  <div class="service-icon"><svg width="30" height="30" viewBox="0 0 30 30"><rect x="3" y="6" width="20" height="20" rx="3" fill="none" stroke="#43a03f" stroke-width="2.5"/><path d="M12 18l2-5 11-11 3 3-11 11z" fill="#43a03f"/></svg></div>
  <div><div class="service-name">Training</div><div class="service-desc">It has survived not only five centu-<br>ries,but also the leap into elec-</div></div>
</div>
<div class="abs service" style="left:442px;top:1545px">
  <div class="service-icon"><svg width="34" height="28" viewBox="0 0 34 28"><circle cx="17" cy="7" r="5" fill="#43a03f"/><circle cx="7" cy="10" r="4" fill="#43a03f"/><circle cx="27" cy="10" r="4" fill="#43a03f"/><path d="M9 26c0-8 16-8 16 0z" fill="#43a03f"/><path d="M1 24c0-6 10-7 10-3v3zM33 24c0-6-10-7-10-3v3z" fill="#43a03f"/></svg></div>
  <div><div class="service-name">Consulting</div><div class="service-desc">It has survived not only five centu-<br>ries,but also the leap into elec-</div></div>
</div>
<div class="abs service" style="left:802px;top:1545px">
  <div class="service-icon"><svg width="32" height="28" viewBox="0 0 32 28"><path d="M2 2v24h28" fill="none" stroke="#43a03f" stroke-width="2.5"/><rect x="8" y="14" width="4" height="10" fill="#43a03f"/><rect x="14" y="8" width="4" height="16" fill="#43a03f"/><rect x="20" y="12" width="4" height="12" fill="#43a03f"/><rect x="26" y="5" width="3" height="19" fill="#43a03f"/></svg></div>
  <div><div class="service-name">Projects</div><div class="service-desc">It has survived not only five centu-<br>ries,but also the leap into elec-</div></div>
</div>

<section id="testimonials">
  <h2 class="abs testi-title">Testimonials</h2>
  <div class="abs testimonial" style="left:112px;top:1940px">
    <div class="avatar" role="img" aria-label="Client portrait"></div>
    <div class="testi-body">
      <p class="quote"><span class="quote-mark quote-open">&ldquo;</span>It is a long established fact that a reader will be distracted by the readable content of a page when looking at its layout. The point of using Lorem <span class="quote-mark">&rdquo;</span></p>
      <div class="person">Hollis Varga</div>
      <div class="role">Dolorem ipsum quia</div>
    </div>
  </div>
  <div class="abs testimonial" style="left:638px;top:1940px">
    <div class="avatar" role="img" aria-label="Client portrait"></div>
    <div class="testi-body">
      <p class="quote"><span class="quote-mark quote-open">&ldquo;</span>It is a long established fact that a reader will be distracted by the readable content of a page when looking at its layout. The point of using Lorem <span class="quote-mark">&rdquo;</span></p>
      <div class="person">Greta Lindqvist</div>
      <div class="role">Porro quisquam</div>
    </div>
  </div>
</section>

<footer class="abs site-footer" id="contact"></footer>
<div class="abs brand footer-brand"><span class="brand-mark"></span><span><span class="brand-name">TALLOWMERE</span><span class="brand-name">LEDGER</span></span></div>

<div class="abs" style="left:365px;top:2254px">
  <div class="f-head">Contact us</div>
  <ul class="f-list">
    <li><svg width="9" height="12" viewBox="0 0 9 12"><path d="M4.5 0a4.5 4.5 0 0 1 4.5 4.5C9 8 4.5 12 4.5 12S0 8 0 4.5A4.5 4.5 0 0 1 4.5 0z" fill="#fff"/><circle cx="4.5" cy="4.5" r="1.6" fill="#222"/></svg><span>Suite 310, 48 Quarry Lane<br>Sydney.</span></li>
    <li><svg width="10" height="10" viewBox="0 0 10 10"><path d="M1 0h3l1 3-2 1a6 6 0 0 0 3 3l1-2 3 1v3c-5 0-9-4-9-9z" fill="#fff"/></svg><span>(555) 014 2290</span></li>
    <li><svg width="11" height="8" viewBox="0 0 11 8"><rect width="11" height="8" fill="#fff"/><path d="M0 0l5.5 4L11 0" fill="none" stroke="#222"/></svg><span>hello@tallowmereledger.com.au</span></li>
  </ul>
</div>

<div class="abs" style="left:646px;top:2254px">
  <div class="f-head">Join our mailing list</div>
  <p class="f-note">Your about us information would fit here nicely.</p>
  <div class="signup"><div class="field">Email address</div><div class="submit">Submit</div></div>
</div>

<div class="abs" style="left:951px;top:2254px">
  <div class="f-head">Follow us out there</div>
  <div class="socials" aria-label="Social profiles"><span></span><span></span><span></span><span></span></div>
</div>

<div class="abs f-rule"></div>
<p class="abs copyright">Copyright &copy; 2017 All Rights Reserved</p>

</body>
</html>
```